Business Card Design

Quiet Meadows - edgy, unique, ontrend clothing for girls 0-12.
I would like simple styling with white background and natural beige/brown font, similar to attached font.

Industry/Entity Type

Clothing

Contact Information for Business Card

Hi, I would like a very simple business card, white background with natural, beige, brown font, Quiet Meadows. I design and sell clothes for girls 0-12 with a touch of bohemian styling. I would like "Quiet Meadows" on front and on back -
www.quietmeadows-example.com.au
Delia Hartwell,
0481552937,
deliahartwell@brightnest-mail.com.au

```html
<!DOCTYPE html>
<html lang="en">
<head>
<meta charset="utf-8">
<title>Quiet Meadows – Business Card</title>
<link rel="stylesheet" href="https://fonts.googleapis.com/css2?family=Short+Stack&display=swap">
<style>
  :root {
    --page-bg: #e6e6e4;
    --card-bg: #ffffff;
    --ink-beige: #a39679;
    --card-shadow: rgba(0, 0, 0, 0.18);
  }
  * { margin: 0; padding: 0; box-sizing: border-box; }
  html, body {
    width: 1200px;
    height: 1000px;
    overflow: hidden;
    background: var(--page-bg);
  }
  body {
    font-family: "Short Stack", "Comic Sans MS", cursive;
    color: var(--ink-beige);
    display: flex;
    flex-direction: column;
    align-items: center;
    justify-content: center;
    gap: 44px;
  }
  .card {
    width: 780px;
    height: 446px;
    background: var(--card-bg);
    box-shadow: 0 8px 22px var(--card-shadow);
    display: flex;
    flex-direction: column;
    align-items: center;
    justify-content: center;
    text-align: center;
  }
  .card-front .brand-name {
    font-size: 92px;
    line-height: 1;
    letter-spacing: 1px;
  }
  .card-front .tagline {
    margin-top: 22px;
    font-size: 22px;
    letter-spacing: 3px;
    text-transform: uppercase;
  }
  .card-back .brand-name {
    font-size: 70px;
    line-height: 1;
  }
  .card-back .holder-name {
    margin-top: 34px;
    font-size: 36px;
    letter-spacing: 6px;
    text-transform: uppercase;
  }
  .contact-list {
    list-style: none;
    margin-top: 26px;
    font-size: 25px;
    line-height: 1.35;
    letter-spacing: 1px;
  }
</style>
</head>
<body>
  <section class="card card-front" aria-label="Business card front">
    <h1 class="brand-name">Quiet Meadows</h1>
    <p class="tagline">Beautiful clothes for girls (age: 0-12)</p>
  </section>

  <section class="card card-back" aria-label="Business card back">
    <h2 class="brand-name">Quiet Meadows</h2>
    <p class="holder-name">Delia Hartwell</p>
    <ul class="contact-list">
      <li class="contact-phone">Phone: 0481552937</li>
      <li class="contact-email">Email: deliahartwell@brightnest-mail.com.au</li>
      <li class="contact-web">Website: www.quietmeadows-example.com.au</li>
    </ul>
  </section>
</body>
</html>
```